Banner ad design for Vantor Reach Ads

We are looking for a designer to develop a concept for banner ads for a Vantor Reach campaign we are building.

We have 3 business lines, shredding services, records management services and scanning services.

We are looking for 4 sets of ads to be created, one for each business line + one set that showcases all of our lines together.

For the design concepts, we would like to see a few sizes (banner, square, leaderboard, skyscraper, etc) for each.

The person chosen will then need to create the ads into all Vantor supported sizes -- 20 sizes total for each set of ads as per the Vantor size guidelines found on this page - https://help.vantor.example/vantor-ads/answer/4859210?hl=en&ref_topic=6082714#

A few items to note:
- Design should complement our existing brand/website look and feel (www.gold-kettle.ca)
- Each final ad must be 150Kb or less in size
- Final designs should be editable, meaning if we would like to change some copy in the design, we can do so using a well-known software (Canva, Photoshop/InDesign, etc)
- Some images are attached for use, but if you feel a different stock image is more suitable to to your design, please go ahead and use it.

Provided below is some messaging that can be used for each set of ads. Do not feel you need to use all of the messaging, it is provided for guidance.

SHREDDING SERVICES:

Possible Short Headline:
-- One-Time Shredding Services
-- Secure Shredding Services
-- Affordable On-Site Shredding

Possible Long Headline
-- Your Paper Can be Destroyed as Soon as the Next Business Day

Possible Descriptions:
-- QVRB AAA Certified On site shredding company. Service as soon as Next Day.
-- Secure and Affordable Toronto & GTA On-Site Shredding.
-- Certified, Affordable Office Shredding Since 2003.
-- Quick, no contact and affordable paper shredding services in Toronto & Southern Ontario.
-- Certified, Affordable Office Shredding Since 2003. Fast, no contact shredding service.

Call to Action
-- Get a Quote

RECORDS MANAGEMENT
Short Headline:
-- Off-site Records Storage
-- Records Management & Storage
-- Secure Records Storage
-- Records Management Services
-- Long Term Records Management
-- Document Storage Solutions

Possible Description
-- Local, Affordable Storage Solutions. Protect and Store your Documents in our Secure Facility
-- Local, Affordable Records Management Solutions. Store your Records in our Secure Facility
-- Certified, Affordable Document Storage Since 2004. Contact Us for a Free Quote!
-- Vaultmark+ Certified, Affordable Document Storage Since 2004. Contact Us for a Free Quote!

Call to Action
-- Get a Quote

SCANNING SERVICES

Short Headline:
-- Professional Scanning Company
-- Toronto & GTA Scanning Service
-- Document Scanning Services
-- Digital Conversion Services
-- Fast & Easy Retrieval

Description
-- Scan and documents and files with Professional scanning services from Gold-Kettle
-- Convert Your Paper Files to Electronic Files. Fast & Easy Retrieval.
-- Easily access your documents electronically with Document Scanning Services

Call to Action
-- Get a Quote

ALL SERVICES AD SET
Short Headline
-- Shred, Scan & Store Documents
-- Secure Shredding, Records Management and Scanning Services
-- #1 Document Management Company
-- Gold Kettle Shredding, Storage & Scanning

Description
-- Secure and Affordable Toronto & GTA On-Site Shredding, Document Storage & Scanning Company

Call to Action
-- Get a Quote

Font styles to use
Sans Serif

```html
<!DOCTYPE html>
<html lang="en">
<head>
<meta charset="utf-8">
<title>Gold-Kettle Banner Ad Set</title>
<link rel="stylesheet" href="https://fonts.googleapis.com/css2?family=Kanit:wght@500&family=Arimo:wght@700&display=swap">
<style>
  :root {
    --bg-top: #1a2270;
    --bg-bottom: #0e4a66;
    --panel-light: #2b80cc;
    --panel-dark: #1a559f;
    --panel-deep: #12407f;
    --swoosh-white: #ffffff;
    --swoosh-green: #3a9a2a;
    --swoosh-blue: #1a4fa0;
    --cta-green: #2f8a1e;
    --cta-green-dark: #1f6512;
    --text-white: #ffffff;
    --head-shadow: #0a2150;
  }
  * { box-sizing: border-box; margin: 0; padding: 0; }
  html, body {
    width: 1200px; height: 1200px; overflow: hidden;
  }
  body {
    background: linear-gradient(180deg, var(--bg-top) 0%, #17326f 45%, var(--bg-bottom) 100%);
    position: relative;
  }
  .banner {
    position: absolute;
    left: 88px;
    width: 1024px;
    height: 256px;
    overflow: hidden;
    box-shadow: 0 6px 16px rgba(0, 0, 0, 0.45);
    background: linear-gradient(135deg, var(--panel-light) 0%, var(--panel-dark) 55%, var(--panel-deep) 100%);
  }
  .banner--storage { top: 36px; }
  .banner--scanning { top: 323px; }
  .banner--shredding { top: 618px; }
  .banner--all { top: 909px; }

  .photo {
    position: absolute;
    left: 0; top: 0;
    width: 540px; height: 256px;
  }
  .photo--shelves {
    background: linear-gradient(90deg, #c9b899 0%, #2f4f9a 18%, #d8ccb4 32%, #2a4a96 48%, #cdbfa4 62%, #e0d6c2 80%, #b9ab90 100%);
  }
  .photo--scanner {
    background: linear-gradient(160deg, #d9d9d6 0%, #f1f0ec 30%, #5a84c8 55%, #e6e4df 75%, #3c3f44 100%);
  }
  .photo--bin {
    background: linear-gradient(170deg, #c8c6c0 0%, #ecebe7 40%, #f6f6f4 60%, #8fd0ea 80%, #3b3b3b 100%);
  }
  .photo--handoff {
    background: linear-gradient(120deg, #efe9e0 0%, #d9c7ae 25%, #7f98b5 50%, #f4f4f2 70%, #c7b8a2 100%);
  }

  .swoosh {
    position: absolute;
    left: 0; top: 0;
    width: 1024px; height: 256px;
  }

  .copy {
    position: absolute;
    left: 510px; right: 0; top: 0; bottom: 0;
    display: flex;
    flex-direction: column;
    align-items: center;
    justify-content: center;
    text-align: center;
    color: var(--text-white);
    padding-left: 10px;
  }
  .headline {
    font-family: "Kanit", sans-serif;
    font-weight: 500;
    font-size: 43px;
    line-height: 44px;
    letter-spacing: 0.5px;
    text-transform: uppercase;
    text-shadow:
      -1.5px -1.5px 0 var(--head-shadow), 1.5px -1.5px 0 var(--head-shadow),
      -1.5px 1.5px 0 var(--head-shadow), 1.5px 1.5px 0 var(--head-shadow),
      2px 3px 4px rgba(0, 0, 0, 0.5);
    white-space: nowrap;
  }
  .frame {
    position: relative;
    margin-top: 12px;
    width: 470px;
    height: 54px;
    border: 1.5px solid var(--text-white);
    display: flex;
    flex-direction: column;
    align-items: center;
    justify-content: center;
    font-family: "Arimo", sans-serif;
    font-weight: 700;
    text-transform: uppercase;
    line-height: 16px;
  }
  .frame__line { font-size: 14.5px; white-space: nowrap; }
  .frame__line--small { font-size: 12px; }
  .corner {
    position: absolute;
    width: 13px; height: 13px;
    border: 1.5px solid var(--text-white);
    background: transparent;
  }
  .corner--tl { left: -7px; top: -7px; }
  .corner--tr { right: -7px; top: -7px; }
  .corner--bl { left: -7px; bottom: -7px; }
  .corner--br { right: -7px; bottom: -7px; }

  .cta {
    margin-top: 13px;
    width: 124px;
    height: 27px;
    border-radius: 3px;
    background: linear-gradient(180deg, #3a9e26 0%, var(--cta-green) 50%, var(--cta-green-dark) 100%);
    box-shadow: 0 2px 3px rgba(0, 0, 0, 0.4);
    font-family: "Arimo", sans-serif;
    font-weight: 700;
    font-size: 14px;
    line-height: 27px;
    letter-spacing: 0.5px;
    color: var(--text-white);
    text-transform: uppercase;
  }
</style>
</head>
<body>

<svg width="0" height="0" style="position:absolute">
  <defs>
    <g id="swoosh-shape">
      <path d="M470 0 Q545 128 500 256 L1024 256 L1024 0 Z" fill="url(#panel-grad)"/>
      <path d="M440 0 Q512 128 468 256" fill="none" stroke="#ffffff" stroke-width="6"/>
      <path d="M452 0 Q525 128 480 256" fill="none" stroke="#3a9a2a" stroke-width="8"/>
      <path d="M463 0 Q537 128 492 256" fill="none" stroke="#1a4fa0" stroke-width="8"/>
      <path d="M505 12 L520 0 M513 20 L537 0 M521 28 L554 0 M529 36 L571 0" stroke="#ffffff" stroke-opacity="0.55" stroke-width="2.5"/>
    </g>
    <linearGradient id="panel-grad" x1="0" y1="0" x2="1" y2="1">
      <stop offset="0" stop-color="#2b80cc"/>
      <stop offset="0.55" stop-color="#1a559f"/>
      <stop offset="1" stop-color="#12407f"/>
    </linearGradient>
  </defs>
</svg>

<section class="banner banner--storage">
  <div class="photo photo--shelves" role="img" aria-label="Warehouse aisle of tall blue shelving stacked with archive boxes"></div>
  <svg class="swoosh" viewBox="0 0 1024 256"><use href="#swoosh-shape"/></svg>
  <div class="copy">
    <h2 class="headline">Secure Records<br>Storage</h2>
    <div class="frame">
      <span class="corner corner--tl"></span><span class="corner corner--tr"></span>
      <span class="corner corner--bl"></span><span class="corner corner--br"></span>
      <p class="frame__line">Local, affordable storage solutions.</p>
      <p class="frame__line frame__line--small">Protect and store your documents in our secure facility</p>
    </div>
    <div class="cta">Get a Qoute</div>
  </div>
</section>

<section class="banner banner--scanning">
  <div class="photo photo--scanner" role="img" aria-label="Hand placing a blue folder on an office scanner glass"></div>
  <svg class="swoosh" viewBox="0 0 1024 256"><use href="#swoosh-shape"/></svg>
  <div class="copy">
    <h2 class="headline">Document<br>Scanning Services</h2>
    <div class="frame">
      <span class="corner corner--tl"></span><span class="corner corner--tr"></span>
      <span class="corner corner--bl"></span><span class="corner corner--br"></span>
      <p class="frame__line frame__line--small">Scan and documents and files with professional</p>
      <p class="frame__line frame__line--small">scanning services from Gold-Kettle</p>
    </div>
    <div class="cta">Get a Qoute</div>
  </div>
</section>

<section class="banner banner--shredding">
  <div class="photo photo--bin" role="img" aria-label="Hand dropping papers into a secure office shredding bin"></div>
  <svg class="swoosh" viewBox="0 0 1024 256"><use href="#swoosh-shape"/></svg>
  <div class="copy">
    <h2 class="headline">Secure Shredding<br>Services</h2>
    <div class="frame">
      <span class="corner corner--tl"></span><span class="corner corner--tr"></span>
      <span class="corner corner--bl"></span><span class="corner corner--br"></span>
      <p class="frame__line">Certified, affordable office shredding since 2003.</p>
      <p class="frame__line">Fast, no contact shredding service.</p>
    </div>
    <div class="cta">Get a Qoute</div>
  </div>
</section>

<section class="banner banner--all">
  <div class="photo photo--handoff" role="img" aria-label="Uniformed service agent receiving a document box in an office"></div>
  <svg class="swoosh" viewBox="0 0 1024 256"><use href="#swoosh-shape"/></svg>
  <div class="copy">
    <h2 class="headline">Shred, Scan &amp; Store<br>Documents</h2>
    <div class="frame">
      <span class="corner corner--tl"></span><span class="corner corner--tr"></span>
      <span class="corner corner--bl"></span><span class="corner corner--br"></span>
      <p class="frame__line frame__line--small">Quick, no contact and affordable paper shredding</p>
      <p class="frame__line frame__line--small">services in Toronto &amp; Southern Ontario</p>
    </div>
    <div class="cta">Get a Qoute</div>
  </div>
</section>

</body>
</html>
```